International professional tennis coach needs a book cover design

This is my 2nd published book, the first one was a #1 on the best seller. I'm looking for a world class book cover design for this new book. The name of my first book was 5 Baseline Habits to Unlock Your Rally Rhythm, located on Brimlow.com

The title of the new book:

Title: The Craft of Steady Rallies
Subtitle: Building a Tactical Margin by Way of Opponent Insight

I'm uploading our new CRAFT OF STEADY logo that I'd like for you to use as the centerpiece of the book design along with a 21st century design feel that incorporates what the book topic is below::

--> This book is about building competitive intelligence by using tennis data analytics to develop and expand a player's strategic advantage for match play. <--

The colors we would like to use are Blue, Yellow, and Green. These shades of these colors should be bold! (You will see the bold color examples of blues, yellows, and greens that I'm talking about in the logos that are attached here, especially the colors for my Tennis GridRally App logo.

I will upload the Tennis GridRally logo which should go somewhere on the back cover design (small size maybe in the bottom corner).

This book is revolutionary to the standard way of teaching tennis, it is based on a decade of recording and gathering tennis data analytics and then we created on-court practice games to develop better decision making in players for the competitive edge.

My websites are www.elevatedrillzone.com and www.craftofsteadyrallies.com

```html
<!DOCTYPE html>
<html lang="en">
<head>
<meta charset="utf-8">
<title>The Craft of Steady Rallies – Cover Wrap</title>
<link href="https://fonts.googleapis.com/css2?family=Jost:wght@500;600;700&family=Lato:ital,wght@0,400;0,700;1,400;1,700&display=swap" rel="stylesheet">
<style>
  :root {
    --page: #ffffff;
    --cover: #0e1512;
    --yellow: #f6c500;
    --blue: #1f7fd8;
    --white: #ffffff;
    --text: #f2f2f2;
    --clay-dark: #3a1d10;
    --clay: #8e4519;
    --clay-light: #b8622a;
  }
  * { box-sizing: border-box; margin: 0; padding: 0; }
  html, body { width: 1200px; height: 706px; overflow: hidden; background: var(--page); }
  .cover-wrap {
    position: absolute; left: 155px; top: 33px;
    width: 890px; height: 640px;
    background: var(--cover);
    overflow: hidden;
    font-family: "Lato", sans-serif;
    color: var(--text);
  }
  /* back cover */
  .back-copy {
    position: absolute; left: 39px; top: 37px; width: 354px;
    font-size: 9.6px; line-height: 11.9px;
  }
  .back-copy p { margin-bottom: 5.5px; }
  .back-copy .tagline { font-weight: 700; font-style: italic; margin-bottom: 5px; }
  .back-copy em, .bio em { font-weight: 700; font-style: italic; }
  .author-photo {
    position: absolute; left: 0; width: 87px; height: 108px;
  }
  .author-photo.first { top: 301px; background: linear-gradient(160deg, #6f7a77, #3a403e 60%, #9a9892); }
  .author-photo.second { top: 434px; background: linear-gradient(170deg, #8fb7dc, #7c6a5e 55%, #34405a); }
  .bio {
    position: absolute; left: 99px; width: 292px;
    font-size: 9.6px; line-height: 11.9px;
  }
  .bio.first { top: 303px; }
  .bio.second { top: 435px; }
  .app-mark {
    position: absolute; left: 12px; top: 566px; width: 70px;
    display: flex; flex-direction: column; align-items: center; gap: 5px;
  }
  .app-mark .dot { width: 30px; height: 30px; border-radius: 50%; background: var(--blue); }
  .app-mark .name {
    font-family: "Jost", sans-serif; font-weight: 600; font-size: 9px;
    color: var(--yellow); text-align: center; line-height: 1.1; text-transform: uppercase;
  }
  .isbn-box {
    position: absolute; left: 252px; top: 536px; width: 132px; height: 84px;
    background: var(--white);
  }
  /* spine */
  .spine {
    position: absolute; left: 427px; top: 0; width: 38px; height: 640px;
  }
  .spine-authors {
    position: absolute; left: 4px; top: 38px;
    writing-mode: vertical-rl;
    font-family: "Jost", sans-serif; font-weight: 500; font-size: 9.5px;
    line-height: 1.2; color: var(--white); letter-spacing: 0.5px;
  }
  .spine-title {
    position: absolute; left: 9px; top: 182px;
    writing-mode: vertical-rl;
    font-family: "Jost", sans-serif; font-weight: 700; font-size: 17px;
    color: var(--yellow); letter-spacing: 0.3px;
  }
  .spine-imprint {
    position: absolute; left: 12px; top: 574px;
    writing-mode: vertical-rl;
    font-family: "Jost", sans-serif; font-weight: 600; font-size: 10px;
    color: var(--yellow);
  }
  /* front cover */
  .front {
    position: absolute; left: 465px; top: 0; width: 425px; height: 640px;
  }
  .front-photo {
    position: absolute; left: 0; top: 232px; width: 425px; height: 408px;
    background: linear-gradient(180deg, var(--cover) 0%, #24170f 22%, var(--clay-dark) 48%, var(--clay) 72%, var(--clay-light) 82%, #4a2412 92%, var(--cover) 100%);
  }
  .front-title {
    position: absolute; left: 0; top: 52px; width: 425px;
    text-align: center;
    font-family: "Jost", sans-serif; font-weight: 700; font-size: 49px;
    line-height: 53px; color: var(--yellow); text-transform: uppercase;
  }
  .front-subtitle {
    position: absolute; left: 0; top: 220px; width: 425px;
    text-align: center;
    font-family: "Jost", sans-serif; font-weight: 600; font-size: 15.5px;
    line-height: 20px; color: var(--blue);
  }
  .front-authors {
    position: absolute; left: 0; top: 593px; width: 425px;
    text-align: center;
    font-family: "Jost", sans-serif; font-weight: 500; font-size: 17px;
    letter-spacing: 0.8px; color: var(--white); text-transform: uppercase;
  }
</style>
</head>
<body>
<main class="cover-wrap">
  <section class="back-cover">
    <div class="back-copy">
      <p class="tagline">A practical guide on how to win more matches by becoming a more efficient and effective competitor.</p>
      <p>As a tennis player you have the ability to play better matches and win more of them. <em>The Craft of Steady Rallies</em> gives you a system to improve. We start with the individual game of the set itself. Our system examines your physical and mental progression, enabling you to upgrade your movement and performance from shot to shot and point to point. Our system seamlessly integrates the technical (physical) aspects with the tactical (mental/emotional) components, providing a comprehensive approach to elevate this performance.</p>
      <p>We aim to give you much more than how to hit great shots. Irrespective of your current skill level, we will provide you with a detailed strategic and tactical plan to enhance your performance, leading to improved results and increased success in your matches.</p>
      <p><em>The Craft of Steady Rallies</em> emphasizes the importance of shifting focus from oneself to the opponent, encouraging players to analyze and understand their adversaries. By bringing the opponent back to the forefront of their thinking, the player creates the best possible context in which to improve as a competitor.</p>
      <p>In this book, we present a groundbreaking approach to tennis data analytics that seamlessly integrates match performance with practice sessions, and vice versa.</p>
    </div>

    <div class="author-photo first" role="img" aria-label="Portrait photo of Corwin Ashdale"></div>
    <p class="bio first">Corwin Ashdale is regarded as one of the leading strategy and tactical coaches in the world today. He is the Creator of <em>Tennis GridRally</em>, the world's first Tennis Tracking App that maps and charts match play based on the rally length of a point. Corwin is a Best Selling Author of the book <em>"5 Baseline Habits to Unlock Your Rally Rhythm"</em> and the Co-Founder of <em>The Craft of Steady Rallies</em> promoting coach, player, and parent development. He is often sought after by coaches around the world to design the practice court in a way that revolutionizes a player's mindset to successfully negotiate the pressures of competitive match play.</p>

    <div class="author-photo second" role="img" aria-label="Portrait photo of Reid Fallon"></div>
    <p class="bio second">Reid Fallon is a writer and tennis coach. He is a Co-Founder at <em>The Craft of Steady Rallies</em> and has been working to create a theoretical framework for tennis players of all levels to improve. Reid studies the forces that act on the player during a tennis match (both internal and external) and works with players to meet the challenge these forces represent. He runs online and on court programs designed specifically to improve a player's Competitive Intelligence.</p>

    <div class="app-mark">
      <span class="dot"></span>
      <span class="name">Tennis GridRally</span>
    </div>
    <div class="isbn-box"></div>
  </section>

  <section class="spine">
    <p class="spine-authors">CORWIN ASHDALE<br>&amp; REID FALLON</p>
    <p class="spine-title">THE CRAFT OF STEADY RALLIES</p>
    <p class="spine-imprint">Veyra</p>
  </section>

  <section class="front">
    <div class="front-photo" role="img" aria-label="Photo of a tennis ball bouncing on a clay court, kicking up a plume of dust"></div>
    <h1 class="front-title">The Craft of<br>Steady<br>Rallies</h1>
    <p class="front-subtitle">Building a Tactical Margin<br>by Way of Opponent Insight</p>
    <p class="front-authors">Corwin Ashdale &amp; Reid Fallon</p>
  </section>
</main>
</body>
</html>
```